Lift Her Forward, 2019 Save The Date

Please develop a save the date flyer our 4th Annual Lift Her Forward and See Her Rise! This event is focused on maintaining participation and appreciation for women in the design and construction industry.

This unique Forum provides a venue to engage everyone from executives to those just beginning their careers with active, hands-on sessions and vibrant networking with the best and brightest in the A/E/C industry. In our usual Q-TarVM Forum style, Keynotes become table participants and table participants become presenters, encouraging participants to assimilate what they are learning. Join local, state and national leaders and subject matter experts as we candidly explore and address the issues affecting women in our industry.

Industry/Entity Type

Construction

Font styles to use
Sans Serif

Requirements
Must have
• This is a save the date, Must have:
• Q-TarVM Logo
• Title: 4th Annual Lift Her Forward and See Her Rise!
• Date: January 25, 2019
• Location: Harbor Crest Resort and Spa, San Marcos, TX
Nice to have
• A header that can easily be pulled to add to other marketing materials and for use across other platforms (web, etc.).

```html
<!DOCTYPE html>
<html lang="en">
<head>
<meta charset="UTF-8">
<title>Lift Her Forward 2019 – Save The Date</title>
<link rel="stylesheet" href="https://fonts.googleapis.com/css2?family=Montserrat:wght@300;400;800&family=Poppins:wght@500;600&family=Stardos+Stencil:wght@700&display=swap">
<style>
  :root {
    --bg: #f2f2f2;
    --paper: #fbfbfb;
    --ink: #111111;
    --green: #8bb33a;
    --ring: #ececec;
    --white: #ffffff;
    --logo-ink: #3a3a3a;
  }
  * { margin: 0; padding: 0; box-sizing: border-box; }
  html, body {
    width: 1200px; height: 960px; overflow: hidden;
    background: var(--bg);
  }
  .flyer {
    position: absolute; left: 322px; top: 88px;
    width: 556px; height: 784px;
    background: var(--paper);
    font-family: 'Montserrat', sans-serif;
  }
  .header {
    position: absolute; top: 74px; left: 0; width: 100%;
    text-align: center;
  }
  .header-title {
    color: var(--ink); line-height: 1; white-space: nowrap;
  }
  .header-ordinal {
    font-weight: 300; font-size: 50px; letter-spacing: -1px;
  }
  .header-name {
    font-weight: 800; font-size: 26px; margin-left: 4px;
  }
  .header-tagline {
    margin-top: 2px;
    color: var(--green); font-weight: 400; font-size: 19.5px; letter-spacing: 0.4px;
  }
  .badge {
    position: absolute; left: 38px; top: 158px;
    width: 480px; height: 480px;
  }
  .badge svg { position: absolute; inset: 0; }
  .badge-text {
    position: absolute; inset: 0;
    display: flex; flex-direction: column; align-items: center; justify-content: center;
    font-family: 'Stardos Stencil', 'Montserrat', sans-serif; font-weight: 700;
    line-height: 0.9;
  }
  .badge-save {
    color: var(--green); font-size: 60px; letter-spacing: 1px; white-space: nowrap;
  }
  .badge-date {
    color: var(--white); font-size: 100px; letter-spacing: 2px; margin-top: 2px;
  }
  .badge-when {
    font-family: 'Montserrat', sans-serif; font-weight: 400;
    color: var(--green); font-size: 16px; letter-spacing: 0.45em;
    margin-top: 18px; margin-right: -0.45em;
  }
  .venue {
    position: absolute; top: 640px; left: 0; width: 100%;
    text-align: center;
    font-family: 'Poppins', sans-serif; font-weight: 600;
    color: var(--green); font-size: 16.5px;
  }
  .organizer {
    position: absolute; top: 690px; left: 0; width: 100%;
    display: flex; flex-direction: column; align-items: center;
  }
  .organizer-mark {
    width: 34px; height: 34px; border-radius: 50%;
    background: var(--green);
  }
  .organizer-name {
    margin-top: 4px;
    font-family: 'Montserrat', sans-serif; font-weight: 400;
    color: var(--logo-ink); font-size: 19px;
  }
</style>
</head>
<body>
  <main class="flyer">
    <header class="header">
      <h1 class="header-title">
        <span class="header-ordinal">4TH</span><span class="header-name">ANNUAL LIFT</span>
      </h1>
      <p class="header-tagline">Her Forward and See Her Rise</p>
    </header>

    <section class="badge">
      <svg viewBox="0 0 480 480" width="480" height="480" aria-hidden="true">
        <circle cx="240" cy="240" r="225" fill="none" stroke="var(--ring)" stroke-width="18"/>
        <circle cx="240" cy="240" r="182" fill="var(--ink)"/>
      </svg>
      <div class="badge-text">
        <span class="badge-save">SAVE THE</span>
        <span class="badge-date">DATE</span>
        <span class="badge-when">JANUARY 25, 2019</span>
      </div>
    </section>

    <p class="venue">Harbor Crest Resort and Spa, San Marcos, TX</p>

    <footer class="organizer">
      <span class="organizer-mark"></span>
      <span class="organizer-name">Q-TarVM</span>
    </footer>
  </main>
</body>
</html>
```